Redesign website bus travel company Lenz Tavan

We require a complete redesign of the website of Reisebüro Lenz Tavan, an established bus tour operator based in Graubünden (www.lenztavan-beispiel.ch). For years, the company has specialized in multi-day tours throughout Europe, as well as day trips such as shopping trips to Innsbruck or Como, music tours, and market visits, primarily for seniors, as well as car rentals for clubs and companies.

The new website requires a video header with overlay text, red as the primary corporate color, complemented by black and gray, and a highly simplified navigation with two main sections: "Our Trips" and "Bus Rental." The remaining sections must be accessible via the "Menu" menu item. The design should be user-friendly for all age groups and mobile-responsive.

The goal is a trustworthy, modern website that reflects personal service and many years of experience.
The new logo can be found in the files, as well as a few pictures.

Target Market(s)

Guests of bus tours (day and multi-day trips) and bus rentals (clubs, companies, etc.)

Industry/Entity Type

Busreisen und Busvermietung

Number of Pages Required

1 page

Requirements
Must have
• Red as primary color, video header, simple UX for target group seniors
Nice to have
• Photo galleries of destinations and the vehicle fleet

```html
<!DOCTYPE html>
<html lang="en">
<head>
<meta charset="utf-8">
<title>Reisebüro Lenz Tavan – Bus Tours Across Europe</title>
<link href="https://fonts.googleapis.com/css2?family=Oswald:wght@500;600&family=Open+Sans:wght@400;600;700&display=swap" rel="stylesheet">
<style>
:root{
  --red:#c8102e;
  --red-dark:#a50d25;
  --black:#1c1c1c;
  --grey-bg:#e9e9e9;
  --grey-text:#555;
  --line:#d0d0d0;
  --white:#fff;
  --footer:#2a2a2a;
  --map-green:#d9e8d6;
  --map-water:#a9d3e6;
  --map-road:#f4f1e8;
}
*{margin:0;padding:0;box-sizing:border-box}
html,body{width:1200px;height:4232px;overflow:hidden}
body{font-family:"Open Sans",Arial,sans-serif;color:var(--black);background:var(--white);position:relative}
.section-title{font-family:"Oswald",Arial,sans-serif;font-weight:500;color:var(--red);font-size:40px;text-align:center}

/* header */
.topbar{position:absolute;top:0;left:0;width:1200px;height:40px;background:var(--white)}
.brand{position:absolute;left:470px;top:0;width:260px;height:40px;background:var(--red);display:flex;align-items:center;justify-content:center;color:var(--white);font-family:"Oswald",sans-serif;font-weight:600;font-size:26px}
.nav{position:absolute;top:40px;left:0;width:1200px;height:50px;display:flex;justify-content:center;align-items:stretch;background:var(--white)}
.nav a{display:flex;align-items:center;gap:8px;padding:0 22px;font-size:15px;font-weight:600;color:var(--black);text-decoration:none}
.nav a.active{background:var(--red);color:var(--white)}

.hero{position:absolute;top:90px;left:0;width:1200px;height:550px}
.hero-media{position:absolute;inset:0;background:linear-gradient(90deg,#1a1f24 0%,#2b3540 38%,#6d8fb3 55%,#8fb06a 80%,#5a7d3c 100%)}
.hero-shade{position:absolute;left:0;top:0;width:560px;height:550px;background:rgba(0,0,0,.35)}
.hero-text{position:absolute;left:112px;top:150px;width:480px;color:var(--white)}
.hero-text h1{font-family:"Oswald",sans-serif;font-weight:600;font-size:42px;line-height:1.2}
.hero-text h1 span{color:var(--red)}
.hero-text p{margin-top:24px;font-size:15px;line-height:1.5;font-weight:600}
.btn{display:inline-block;background:var(--red);color:var(--white);font-size:14px;font-weight:600;padding:8px 22px;border-radius:3px;text-decoration:none}
.hero-text .btn{margin-top:22px}
.play{position:absolute;left:860px;top:235px}

/* trips */
.trips{position:absolute;top:640px;left:0;width:1200px;height:500px}
.trips .section-title{position:absolute;top:52px;width:100%}
.trip-card{position:absolute;top:155px;width:300px}
.trip-img{height:200px;border-radius:3px}
.trip-card h3{margin-top:18px;font-size:16px;font-weight:700}
.trip-card .bar{margin-top:8px;width:40px;height:3px;background:var(--red)}
.arrow-btn{position:absolute;top:237px}

/* about */
.about{position:absolute;top:1140px;left:0;width:1200px;height:540px;background:var(--grey-bg)}
.about .title{position:absolute;left:112px;top:75px;font-family:"Oswald",sans-serif;font-weight:500;color:var(--red);font-size:40px}
.about h3{position:absolute;left:112px;top:145px;font-size:18px;font-weight:700}
.about p{position:absolute;left:112px;top:180px;width:470px;font-size:14px;line-height:1.55;color:var(--grey-text)}
.about .btn{position:absolute;left:112px;top:400px}
.about-photo{position:absolute;left:600px;top:70px;width:470px;height:390px;border-radius:45% 40% 42% 48%}

/* rental */
.rental{position:absolute;top:1680px;left:0;width:1200px;height:980px}
.rental .section-title{position:absolute;top:55px;width:100%}
.rental-frame{position:absolute;left:100px;top:160px;width:330px;height:390px;background:var(--red)}
.rental-photo{position:absolute;left:135px;top:145px;width:380px;height:370px}
.form{position:absolute;left:628px;top:160px;width:460px}
.form h3{font-size:20px;font-weight:700}
.form .sub{font-size:12px;color:var(--grey-text);margin-top:6px}
.fields{margin-top:16px;display:grid;grid-template-columns:1fr 1fr;gap:14px 16px}
.field{height:32px;border:1px solid var(--line);border-radius:3px;font-size:12px;color:#888;display:flex;align-items:center;padding:0 10px}
.form .btn{margin-top:18px}
.info{position:absolute;width:440px}
.info h4{font-family:"Oswald",sans-serif;font-weight:500;color:var(--red);font-size:24px}
.info p{margin-top:8px;font-size:13px;line-height:1.55;color:var(--grey-text)}

/* download */
.download{position:absolute;top:2660px;left:180px;width:840px;height:160px;background:var(--red);z-index:2;color:var(--white)}
.download h3{position:absolute;left:72px;top:40px;font-family:"Oswald",sans-serif;font-weight:500;font-size:30px}
.download p{position:absolute;left:72px;top:92px;width:520px;font-size:13px;line-height:1.5;font-weight:600}
.download .btn{position:absolute;right:72px;top:60px;background:var(--white);color:var(--red);padding:8px 38px}

/* map */
.map{position:absolute;top:2760px;left:0;width:1200px;height:480px;overflow:hidden}
.map-base{position:absolute;inset:0;background:linear-gradient(160deg,var(--map-green) 0%,#cfe3d2 35%,var(--map-water) 55%,#e4ebe2 80%,var(--map-green) 100%)}
.place-card{position:absolute;left:600px;top:210px;width:300px;height:118px;background:var(--white);border-radius:8px;box-shadow:0 2px 8px rgba(0,0,0,.25);padding:10px;display:flex;gap:10px;z-index:1}
.place-thumb{width:84px;height:98px;border-radius:5px;background:linear-gradient(160deg,#c8102e,#7a0a1c)}
.place-info{flex:1;font-size:11px;line-height:1.5;color:var(--grey-text)}
.place-info strong{display:block;font-size:13px;color:var(--black)}
.place-info .stars{color:#e8a317}
.place-info .closed{color:var(--red)}
.place-actions{display:flex;gap:8px;margin-top:4px}
.place-actions i{display:block;width:24px;height:24px;border-radius:50%;background:#e8eef7}
.map-pin{position:absolute;left:736px;top:330px;z-index:1}

/* photos */
.photos{position:absolute;top:3240px;left:0;width:1200px;height:700px}
.photos .section-title{position:absolute;top:80px;width:100%}
.ph{position:absolute;border-radius:14px}
.ph-feature{position:absolute;left:440px;top:160px;width:312px;height:500px;background:linear-gradient(180deg,#d21c35,#b40f27);border-radius:14px;color:var(--white);text-align:center}
.ph-feature span{position:absolute;top:300px;left:0;width:100%;font-family:"Oswald",sans-serif;font-weight:500;font-size:22px}

/* footer */
.footer{position:absolute;top:3940px;left:0;width:1200px;height:292px;background:var(--footer);color:var(--white)}
.footer-brand{position:absolute;left:112px;top:70px;font-family:"Oswald",sans-serif;font-weight:600;font-size:34px}
.social{position:absolute;left:112px;top:135px;display:flex;gap:10px}
.social i{display:block;width:34px;height:34px;border:2px solid var(--white);border-radius:50%}
.fcol{position:absolute;top:66px;font-size:13px;line-height:1.6}
.fcol strong{display:block;font-size:16px;margin-bottom:6px}
.copyright{position:absolute;left:0;bottom:20px;width:100%;text-align:center;font-size:12px;font-weight:600}
</style>
</head>
<body>

<header>
  <div class="topbar"><div class="brand">Lenz Tavan</div></div>
  <nav class="nav">
    <a class="active" href="#">Home</a>
    <a href="#">Our Trips</a>
    <a href="#">Bus Rental</a>
    <a href="#"><svg width="18" height="14" viewBox="0 0 18 14"><rect y="0" width="18" height="2" fill="#1c1c1c"/><rect y="6" width="18" height="2" fill="#1c1c1c"/><rect y="12" width="18" height="2" fill="#1c1c1c"/></svg>Menu</a>
  </nav>
</header>

<section class="hero">
  <div class="hero-media" role="img" aria-label="Video still of a red and white touring coach driving through a green alpine landscape"></div>
  <div class="hero-shade"></div>
  <div class="hero-text">
    <h1>Comfortable <span>Bus Tours Across Europe</span> – With Heart &amp; Experience</h1>
    <p>Over 60 Years Has Been Run By Marco Sennhauser &amp; Petra Caduff, The Fourth Generation Of The Family, Since August 1, 2013</p>
    <a class="btn" href="#">View Our Trips</a>
  </div>
  <svg class="play" width="76" height="76" viewBox="0 0 76 76"><circle cx="38" cy="38" r="38" fill="#c8102e"/><path d="M30 24 L54 38 L30 52 Z" fill="#fff"/></svg>
</section>

<section class="trips">
  <h2 class="section-title">Our Trips</h2>
  <svg class="arrow-btn" style="left:42px" width="36" height="36" viewBox="0 0 36 36"><circle cx="18" cy="18" r="16" fill="#fff" stroke="#1c1c1c" stroke-width="2"/><path d="M21 11 L14 18 L21 25" fill="none" stroke="#1c1c1c" stroke-width="3"/></svg>
  <div class="trip-card" style="left:112px"><div class="trip-img" role="img" aria-label="Old town street with half-timbered houses" style="background:linear-gradient(160deg,#8aa3b8,#b59a7c 60%,#6f5a48)"></div><h3>Day Trips</h3><div class="bar"></div></div>
  <div class="trip-card" style="left:450px"><div class="trip-img" role="img" aria-label="White coach parked on a road" style="background:linear-gradient(170deg,#dfe4e8,#b9c0c6 60%,#8b9198)"></div><h3>Holiday Trips</h3><div class="bar"></div></div>
  <div class="trip-card" style="left:788px"><div class="trip-img" role="img" aria-label="Coastal bay with turquoise water and harbour" style="background:linear-gradient(170deg,#9fc6e2,#3fa6b8 55%,#6d8a5a)"></div><h3>Club Trips</h3><div class="bar"></div></div>
  <svg class="arrow-btn" style="left:1122px" width="36" height="36" viewBox="0 0 36 36"><circle cx="18" cy="18" r="16" fill="#fff" stroke="#1c1c1c" stroke-width="2"/><path d="M15 11 L22 18 L15 25" fill="none" stroke="#1c1c1c" stroke-width="3"/></svg>
</section>

<section class="about">
  <h2 class="title">About Us</h2>
  <h3>Experience The World With Us</h3>
  <p>The Lenz Tavan Travel Agency Was Founded Over 60 Years Ago And Has Been Run By Marco Sennhauser And Petra Caduff Since August 1, 2013. Our Team Combines Expertise, Friendly And Reliable Service, And Competitive Prices. Our Team Of Nina Brunold, Lea Joos And Our Office Staff Will Be Happy To Assist You With Travel Arrangements. Our Experienced And Friendly Chauffeurs Will Ensure That You Reach Your Destination Safely And Comfortably.</p>
  <a class="btn" href="#">Read More</a>
  <div class="about-photo" role="img" aria-label="Smiling travel host in uniform in front of a coach" style="background:radial-gradient(circle at 50% 45%,#e9e2da,#c9c2bb 60%,#5d6066)"></div>
</section>

<section class="rental">
  <h2 class="section-title">Bus Rental</h2>
  <div class="rental-frame"></div>
  <div class="rental-photo" role="img" aria-label="Silver minibus on a mountain road" style="background:linear-gradient(170deg,#a9bed4,#c5ccd2 45%,#7d8a74)"></div>
  <div class="form">
    <h3>Reservation Request</h3>
    <div class="sub">Our Rental Reservation Request</div>
    <div class="fields">
      <div class="field">Company/Association</div><div class="field">Name</div>
      <div class="field">First Name</div><div class="field">Address</div>
      <div class="field">ZIP / City</div><div class="field">Phone</div>
      <div class="field">E-mail</div><div class="field">Hour</div>
      <div class="field">Start Date</div><div class="field">End Date</div>
    </div>
    <a class="btn" href="#">Submit</a>
  </div>
  <div class="info" style="left:112px;top:620px"><h4>Price</h4><p>CHF 250.00, Seven-Day rate per day including 200 km<br>CHF 0.85 per additional kilometre<br>(Prices include 8.1% VAT, fuel extra and driver)</p></div>
  <div class="info" style="left:640px;top:620px"><h4>Chauffeur</h4><p>If you don't want to drive the vehicle yourself, we'll be happy to provide a driver. The price depends on the date, time of use, etc. Please contact us directly.</p></div>
  <div class="info" style="left:112px;top:740px"><h4>Extra costs</h4><p>CHF 30.00, final interior cleaning<br>CHF 60.00, final interior and exterior cleaning<br>CHF 50.00, goods transport trailer (total weight 750 kg)</p></div>
  <div class="info" style="left:640px;top:740px"><h4>Requirements For A Driving License</h4><p>Driving license category D1</p></div>
</section>

<section class="download">
  <h3>Travel Program 2025 As Download</h3>
  <p>Our travel industry expertise, friendly and reliable service, and competitive prices set us apart from the competition.</p>
  <a class="btn" href="#">Download</a>
</section>

<section class="map">
  <div class="map-base" role="img" aria-label="Map of the river valley around the office of Reisebüro Lenz Tavan"></div>
  <div class="place-card">
    <div class="place-thumb" role="img" aria-label="Red coaches of the company fleet"></div>
    <div class="place-info">
      <strong>Reisebüro Lenz Tavan</strong>
      4.6 <span class="stars">★★★★★</span> (37)<br>
      Travel agency<br>
      <span class="closed">Closed</span> · Opens 7:30 am
      <div class="place-actions"><i></i><i></i><i></i></div>
    </div>
  </div>
  <svg class="map-pin" width="28" height="38" viewBox="0 0 28 38"><path d="M14 1 C6 1 1 7 1 14 C1 24 14 37 14 37 C14 37 27 24 27 14 C27 7 22 1 14 1 Z" fill="#c8102e"/><circle cx="14" cy="14" r="5" fill="#fff"/></svg>
</section>

<section class="photos">
  <h2 class="section-title">Photo's From Destinations</h2>
  <div class="ph" style="left:112px;top:160px;width:300px;height:240px;background:linear-gradient(160deg,#b59268,#8b6a4a 60%,#6c7c86)" role="img" aria-label="Historic town with bridge over a canal"></div>
  <div class="ph" style="left:112px;top:430px;width:300px;height:230px;background:linear-gradient(180deg,#8fb4d6,#c9d8e3 55%,#a9b7bd)" role="img" aria-label="Lake shore with a pier"></div>
  <div class="ph-feature">
    <svg style="position:absolute;left:126px;top:210px" width="60" height="76" viewBox="0 0 60 76"><path d="M30 2 C14 2 4 14 4 28 C4 46 30 74 30 74 C30 74 56 46 56 28 C56 14 46 2 30 2 Z" fill="#fff"/><circle cx="30" cy="28" r="10" fill="#c8102e"/></svg>
    <span>Southeast Switzerland</span>
  </div>
  <div class="ph" style="left:780px;top:160px;width:308px;height:240px;background:linear-gradient(170deg,#b8c9db,#9aa9b4 50%,#6d7a5c)" role="img" aria-label="Mountain village in a valley"></div>
  <div class="ph" style="left:780px;top:430px;width:308px;height:230px;background:linear-gradient(170deg,#a9bfd8,#8c7fb0 55%,#7a6a9c)" role="img" aria-label="Lavender fields in front of an old abbey"></div>
</section>

<footer class="footer">
  <div class="footer-brand">Lenz Tavan</div>
  <div class="social"><i></i><i></i></div>
  <div class="fcol" style="left:480px"><strong>Travel Agency Lenz Tavan</strong>c/o Marco Sennhauser Car-Reisen AG<br>Talweg 8<br>CH-7099 Musterdorf</div>
  <div class="fcol" style="left:760px"><strong>Phone</strong>+41 (0)81 000 12 34</div>
  <div class="fcol" style="left:960px"><strong>Mail</strong>info@lenztavan-beispiel.ch</div>
  <div class="copyright">Copyright © 2025 Lenz Tavan. All rights reserved.</div>
</footer>

</body>
</html>
```